Front and back label for Men’s Beard and Face Lotion

Slogan to include somewhere on the label: STAY WILD. STAY BEARDED.

We have created a men’s face and beard lotion for our company, Ridgefern Beard Company, a subsidiary of Kestrel Lather Co. we need new labels for our entire men’s grooming line but we’re starting with the face/beard lotion with the idea that the style of that label will be able to carry across to the beard balms, oils, etc. I’ll upload our temporary logo, but we have a logo designer working on our permanent logo right now, should have it in a couple of days.

For the size: 1.5in (38.1mm) wide x 2.5in (63.5mm) tall.

Bottle is a dark green rectangular pump bottle. Color scheme needs to not clash. I’ll upload an AI rendering to give more info, though whatever you come up with does not have to copy the rendering. It’s simply a style that I liked.

We don’t want to look too much like the other beard brands out there with their “refined vintage gentleman” look. We’re rough around the edges, very outdoorsman and mountain oriented. Bright colors used to draw attention is totally fine. Our name comes from the Ridgefern Mountains in Idaho, US.

Target Market(s)

Bearded Men ages 20-death. Also some appeal to their partners.

Industry/Entity Type

Cosmetics labels, hair and skincare

Requirements
Must have
• The URL : RidgefernBeard.example on the back label. A spot on the back for a UPC. Proper bleed layout for Corvane Label printing requirements.
Nice to have
• A design that we can hire the designer to base other product designs off of. A foundation-design vibe, in a sense. This project could lead to 10 more designs already planned.
Should not have
• Pink, purple, too generic of a beard vibe. We want this to look Cool.

```html
<!DOCTYPE html>
<html lang="en">
<head>
<meta charset="utf-8">
<title>Ridgefern Face &amp; Beard Lotion Labels</title>
<link href="https://fonts.googleapis.com/css2?family=Archivo:wght@400;700;800&family=Jost:wght@600;700&display=swap" rel="stylesheet">
<style>
  :root {
    --page: #e4e3e0;
    --forest: #0f5a33;
    --forest-deep: #0c2a1c;
    --ink: #0b1110;
    --accent: #17a455;
    --accent-bright: #1fb35e;
    --cream: #f1ead8;
    --white: #ffffff;
  }
  * { box-sizing: border-box; margin: 0; padding: 0; }
  html, body { width: 972px; height: 1200px; overflow: hidden; }
  body {
    background: var(--page);
    font-family: "Archivo", Arial, sans-serif;
    position: relative;
  }
  .label {
    position: absolute;
    top: 252px;
    width: 430px;
    height: 695px;
    overflow: hidden;
    box-shadow: 0 6px 14px rgba(0,0,0,0.25);
    text-align: center;
  }
  .label--front { left: 36px; background: linear-gradient(180deg, var(--forest) 0%, var(--forest-deep) 55%, var(--ink) 82%); }
  .label--back { left: 506px; background: var(--ink); }

  .front__corner { position: absolute; top: 0; right: 0; width: 84px; height: 84px; }
  .front__art {
    position: absolute; left: 40px; top: 31px; width: 350px; height: 146px;
    background: linear-gradient(180deg, #d9d6cc 0%, #5d6a68 45%, #1c2622 100%);
    border-radius: 4px;
  }
  .brand {
    position: absolute; left: 0; right: 0; top: 176px;
    font-family: "Jost", sans-serif; font-weight: 700; color: var(--cream);
  }
  .brand__name { display: block; font-size: 60px; line-height: 64px; letter-spacing: 1px; }
  .brand__sub { display: block; font-size: 17px; letter-spacing: 5px; margin-top: 4px; }
  .product__kind {
    position: absolute; left: 0; right: 0; top: 276px;
    font-family: "Jost", sans-serif; font-weight: 700; color: var(--cream);
    font-size: 46px; line-height: 54px;
  }
  .product__name {
    position: absolute; left: 0; right: 0; top: 326px;
    font-family: "Jost", sans-serif; font-weight: 700; color: var(--accent);
    font-size: 94px; line-height: 94px; letter-spacing: -2px;
  }
  .scent-pill {
    position: absolute; left: 43px; top: 434px; width: 345px; height: 42px;
    border-radius: 21px;
    background: linear-gradient(180deg, #26a55c 0%, #0e6b39 100%);
    color: var(--cream); font-weight: 800; font-size: 25px; letter-spacing: 5px;
    line-height: 42px;
  }
  .key-ingredients {
    position: absolute; left: 0; right: 0; top: 487px;
    color: var(--cream); font-size: 19px; line-height: 24px; letter-spacing: 0.5px;
  }
  .net-volume {
    position: absolute; left: 0; right: 0; top: 542px;
    color: var(--accent); font-size: 19px; font-weight: 700;
  }
  .front__rule { position: absolute; left: 0; right: 0; top: 572px; height: 6px; background: var(--accent); }
  .slogan {
    position: absolute; left: 0; right: 0; top: 589px;
    color: var(--cream); font-weight: 800; font-size: 30px; line-height: 37px; letter-spacing: 2px;
  }

  .back__header {
    height: 97px;
    background: linear-gradient(180deg, var(--forest) 0%, var(--forest-deep) 100%);
    padding-top: 25px;
    color: var(--cream);
  }
  .back__brand { font-weight: 800; font-size: 40px; line-height: 38px; letter-spacing: 4px; }
  .back__product { font-weight: 800; font-size: 19px; letter-spacing: 1.5px; margin-top: 4px; }
  .back__rule { height: 6px; background: var(--accent); }
  .back__body { padding: 14px 42px 0 42px; text-align: left; }
  .section-title { color: var(--accent); font-weight: 800; font-size: 19px; letter-spacing: 2.5px; line-height: 24px; }
  .section-text { color: var(--white); font-size: 17.5px; line-height: 22px; margin-top: 2px; }
  .section-divider { height: 1px; background: var(--accent); margin: 8px 0 8px; }
  .upc-area {
    position: absolute; left: 45px; top: 419px; width: 340px; height: 215px;
    background: var(--white);
  }
  .site-url {
    position: absolute; left: 0; right: 0; top: 640px;
    color: var(--accent-bright); font-weight: 700; font-size: 22px;
  }
</style>
</head>
<body>
  <section class="label label--front">
    <svg class="front__corner" viewBox="0 0 84 84" aria-hidden="true"><polygon points="0,0 84,0 84,84" fill="#17a455"/></svg>
    <div class="front__art" role="img" aria-label="Illustration of snowy mountain peaks framed by pine trees"></div>
    <div class="brand">
      <span class="brand__name">RIDGEFERN</span>
      <span class="brand__sub">BEARD COMPANY</span>
    </div>
    <h1 class="product__kind">FACE &amp; BEARD</h1>
    <div class="product__name">LOTION</div>
    <div class="scent-pill">UNSCENTED</div>
    <p class="key-ingredients">ALOE VERA + NIACINAMIDE<br>ARGAN OIL</p>
    <p class="net-volume">3.4 FL OZ (100 mL)</p>
    <div class="front__rule"></div>
    <p class="slogan">STAY WILD.<br>STAY BEARDED.</p>
  </section>

  <section class="label label--back">
    <header class="back__header">
      <div class="back__brand">RIDGEFERN</div>
      <div class="back__product">FACE &amp; BEARD LOTION</div>
    </header>
    <div class="back__rule"></div>
    <div class="back__body">
      <h2 class="section-title">DIRECTIONS</h2>
      <p class="section-text">Apply daily. Massage one pump into skin and beard until absorbed. Brush or comb through. Follow with beard oil or balm and style as desired.</p>
      <div class="section-divider"></div>
      <h2 class="section-title">INGREDIENTS</h2>
      <p class="section-text">Water, Aloe Barbadensis Leaf Juice, Simmondsia Chinensis (Jojoba) Seed Oil, Propanediol, Argania Spinosa Kernel Oil, Panthenol, IBT-50, Niacinamide, Cetyl Alcohol, Phenoxyethanol (and) Caprylyl Glycol.</p>
    </div>
    <div class="upc-area" aria-label="Space for UPC"></div>
    <p class="site-url">RidgefernBeard.example</p>
  </section>
</body>
</html>
```